Silverpine Orbit Works Flyer

We need a one page promotional piece that explains what our company does, and the benefits it provides in a simple, elegant, easy to understand way. I would like to print it on glossy heavyweight paper to give a feel of high quality and legitimacy. I will include the logo, the tag line, and the main benefits that the company offers.

Tag line concept, may not need these exact words. "Lend us 5 minutes each morning, and we will guide you toward a Silverpine Orbit Works."

Key points...(exact wording not required if you think of a better way to say it)

Software easy enough for my grandpa to use.
Lets you use snail mail, email, texting, and social media to quickly market to your customers at very low cost.
Web based which allows you to launch media campaigns from your desktop, or smartphone in moments.
Quick 3 - 5 minute training videos which give you hard hitting, quick action tips that will help you make your business better today.
Live coaching calls to help motivate you to improve your business.
No contracts, or start up fees. One low price of $299 per month.

Restaurant owners

Restaurant

```html
<!DOCTYPE html>
<html lang="en">
<head>
<meta charset="utf-8">
<title>Silverpine Orbit Works Flyer</title>
<link href="https://fonts.googleapis.com/css2?family=Lato:ital,wght@0,400;0,700;0,900;1,400;1,700&display=swap" rel="stylesheet">
<style>
  :root {
    --backdrop: #dcdcdc;
    --paper: #ffffff;
    --paper-fade: #ececec;
    --ink: #4a4a4a;
    --ink-soft: #3c3c3c;
    --brand-grey: #7a7a7a;
    --green: #5f9a2c;
    --green-deep: #4e8a22;
    --green-panel: rgba(128, 160, 72, 0.9);
    --photo-dark: #2e221b;
    --photo-mid: #6b4a32;
    --photo-warm: #d9b98a;
  }
  * { box-sizing: border-box; margin: 0; padding: 0; }
  html, body { width: 1200px; height: 900px; overflow: hidden; }
  body {
    background: radial-gradient(circle at 50% 40%, #f2f2f2, var(--backdrop));
    font-family: "Lato", Arial, sans-serif;
    color: var(--ink);
  }
  .flyer {
    position: absolute;
    left: 290px; top: 20px;
    width: 620px; height: 860px;
    display: flex; flex-direction: column;
    background: linear-gradient(to bottom, var(--paper) 60%, var(--paper-fade));
    box-shadow: 0 10px 30px rgba(0,0,0,0.25);
    overflow: hidden;
  }
  .brand {
    flex: none; height: 96px;
    display: flex; align-items: center; justify-content: center; gap: 14px;
  }
  .brand-dot {
    width: 38px; height: 38px; border-radius: 50%;
    border: 3px solid #8a8a8a;
  }
  .brand-name {
    font-weight: 900; font-size: 32px; color: var(--brand-grey);
    letter-spacing: 1px; text-transform: uppercase;
  }
  .hero { flex: none; position: relative; height: 370px; }
  .hero-photo {
    position: absolute; inset: 0;
    background:
      linear-gradient(to bottom, transparent 55%, rgba(217,185,138,0.9) 62%, var(--photo-mid) 72%, var(--photo-dark)),
      linear-gradient(100deg, var(--photo-dark) 0%, var(--photo-mid) 45%, #b7a48a 80%);
  }
  .tagline-panel {
    position: absolute; right: 0; top: 30px;
    width: 250px; height: 340px;
    background: var(--green-panel);
    color: #fff; text-align: center;
    padding: 18px 10px 0;
  }
  .tag-lead { font-style: italic; font-size: 27px; line-height: 1.2; }
  .tag-big { font-weight: 900; font-size: 40px; line-height: 1; margin-top: 4px; }
  .tag-mid { font-weight: 900; font-size: 23px; line-height: 1.05; margin-top: 8px; }
  .tag-box {
    display: inline-block; background: #fff; color: var(--green-deep);
    font-weight: 900; font-size: 14px; line-height: 1.2;
    padding: 3px 8px; margin-top: 8px; text-transform: uppercase;
  }
  .tag-url { font-weight: 700; font-size: 15px; margin-top: 14px; }
  .offer { flex: none; text-align: center; margin-top: 16px; }
  .offer-terms { font-weight: 700; font-size: 26px; line-height: 1.25; color: var(--ink); }
  .offer-price { font-weight: 700; font-size: 26px; line-height: 1.25; color: var(--green); }
  .benefits { flex: none; list-style: none; margin: 14px 34px 0 36px; }
  .benefits li {
    display: flex; align-items: flex-start; gap: 10px;
    font-style: italic; font-size: 14.5px; line-height: 1.2;
    color: var(--ink-soft); margin-bottom: 10px;
  }
  .benefits li:last-child { margin-bottom: 0; }
  .tick { flex: none; width: 24px; height: 24px; }
  .contact {
    flex: none; margin: auto 36px 40px 40px;
    display: flex; align-items: flex-end; justify-content: space-between;
  }
  .contact-url { color: var(--green); font-size: 15px; text-transform: uppercase; }
  .contact-phone {
    display: flex; align-items: center; gap: 10px;
    color: var(--green); font-size: 27px; font-weight: 700;
  }
  .footer-band {
    position: absolute; left: 0; right: 0; bottom: 0; height: 18px;
    background: var(--green);
  }
</style>
</head>
<body>
  <main class="flyer">
    <header class="brand">
      <span class="brand-dot"></span>
      <span class="brand-name">Silverpine Orbit Works</span>
    </header>

    <section class="hero">
      <div class="hero-photo" role="img" aria-label="Photo of a modern restaurant bar counter with stools, shelves of bottles and cocktails"></div>
      <div class="tagline-panel">
        <p class="tag-lead">Lend us</p>
        <p class="tag-big">5 MIN<br>EACH<br>MORNING</p>
        <p class="tag-mid">AND WE WILL<br>GUIDE YOU</p>
        <p class="tag-box">Toward a Silverpine<br>Orbit Works</p>
        <p class="tag-url">www.silverpineorbit.com</p>
      </div>
    </section>

    <section class="offer">
      <h2 class="offer-terms">No contracts, or start up fees</h2>
      <p class="offer-price">One low price of $299 per month</p>
    </section>

    <ul class="benefits">
      <li><svg class="tick" viewBox="0 0 24 24"><rect width="24" height="24" rx="3" fill="#5f9a2c"/><path d="M6 12.5l4 4 8-9" stroke="#fff" stroke-width="3" fill="none"/></svg>Software easy enough for your grandpa to use.</li>
      <li><svg class="tick" viewBox="0 0 24 24"><rect width="24" height="24" rx="3" fill="#5f9a2c"/><path d="M6 12.5l4 4 8-9" stroke="#fff" stroke-width="3" fill="none"/></svg>Lets you use snail mail, email, texting, and social media to quickly market to your customers at very low cost.</li>
      <li><svg class="tick" viewBox="0 0 24 24"><rect width="24" height="24" rx="3" fill="#5f9a2c"/><path d="M6 12.5l4 4 8-9" stroke="#fff" stroke-width="3" fill="none"/></svg>Web based which allows you to launch media campaigns from your desktop, or smartphone in moments.</li>
      <li><svg class="tick" viewBox="0 0 24 24"><rect width="24" height="24" rx="3" fill="#5f9a2c"/><path d="M6 12.5l4 4 8-9" stroke="#fff" stroke-width="3" fill="none"/></svg>Quick 3 - 5 minute training videos which give you hard hitting, quick action tips that will help you make your business better today.</li>
      <li><svg class="tick" viewBox="0 0 24 24"><rect width="24" height="24" rx="3" fill="#5f9a2c"/><path d="M6 12.5l4 4 8-9" stroke="#fff" stroke-width="3" fill="none"/></svg>Live coaching calls to help motivate you to improve your business.</li>
    </ul>

    <footer class="contact">
      <span class="contact-url">www.silverpineorbit.com</span>
      <span class="contact-phone">
        <svg width="34" height="34" viewBox="0 0 34 34" aria-hidden="true">
          <rect width="34" height="34" rx="4" fill="#5f9a2c"/>
          <path d="M7 12c0-3 3-5 10-5s10 2 10 5v2h-5v-3h-10v3H7z" fill="#fff"/>
          <rect x="9" y="16" width="16" height="11" rx="2" fill="#fff"/>
          <g fill="#5f9a2c"><circle cx="13" cy="19.5" r="1.2"/><circle cx="17" cy="19.5" r="1.2"/><circle cx="21" cy="19.5" r="1.2"/><circle cx="13" cy="23.5" r="1.2"/><circle cx="17" cy="23.5" r="1.2"/><circle cx="21" cy="23.5" r="1.2"/></g>
        </svg>
        014-726-390
      </span>
    </footer>
    <div class="footer-band"></div>
  </main>
</body>
</html>
```